Stationery design for law/Property/finance business

We need stationery design for a Law/Property/Finance business called Ridgemoor. Logo is attached.
we require a letterhead and with compliments slip.
Would like to see a very simple professional design using the colours of the logo and offset against Charcoal colours. Maybe a charcoal band for header and footer with logo and details appearing in it? Former letterhead attached for examples.
we require the project to be provided in word, pdf and jpeg format.
we require the following details on the stationery:
Cairns Phone: 07 40551926
Weipa Phone: 07 40613847
Mobile: 0491 570 384
Fax: 07 40338172
email: admin@ridgemoorholdings-example.com.au
ABN 51 824 306 917

```html
<!DOCTYPE html>
<html lang="en">
<head>
<meta charset="utf-8">
<title>Ridgemoor Stationery</title>
<link href="https://fonts.googleapis.com/css2?family=Montserrat:wght@600;700&family=Questrial&display=swap" rel="stylesheet">
<style>
  :root {
    --ocean: #0a8fcf;
    --lagoon: #33b8a0;
    --mist: #808080;
    --charcoal: #5f5f5f;
    --ink: #111111;
    --paper: #ffffff;
    --band-h: linear-gradient(90deg, var(--ocean) 0%, var(--lagoon) 25%, var(--mist) 50%, var(--charcoal) 100%);
    --band-v: linear-gradient(180deg, var(--ocean) 0%, var(--lagoon) 26%, var(--mist) 52%, var(--charcoal) 74%, var(--charcoal) 100%);
  }
  html, body { margin: 0; padding: 0; overflow: hidden; }
  body { width: 1200px; height: 1200px; background: var(--paper); position: relative; font-family: "Montserrat", sans-serif; }

  .letterhead-header {
    position: absolute; left: 28px; top: 36px; width: 798px; height: 118px;
    background: var(--band-h);
  }
  .letterhead-header .brand-name {
    position: absolute; right: 18px; top: 60px;
    font-family: "Montserrat", sans-serif; font-weight: 700; font-size: 32px;
    letter-spacing: 1px; color: var(--paper); text-transform: uppercase; line-height: 1;
  }

  .letterhead-footer {
    position: absolute; left: 28px; top: 1103px; width: 798px; height: 60px;
    background: var(--band-h); overflow: hidden;
    color: var(--ink); font-weight: 700; font-size: 13px; line-height: 19px;
  }
  .footer-col { position: absolute; top: 11px; white-space: nowrap; }
  .footer-col.phones { left: 18px; }
  .footer-col.mobile { left: 228px; }
  .footer-col.online { left: 410px; }

  .business-card {
    position: absolute; left: 883px; top: 362px; width: 288px; height: 475px;
    background: var(--band-v); color: var(--paper); overflow: hidden;
  }
  .vertical { position: absolute; writing-mode: vertical-rl; white-space: nowrap; }
  .card-name {
    left: 141px; top: 60px; width: 24px;
    font-family: "Questrial", sans-serif; font-size: 22px; letter-spacing: 14px; line-height: 24px;
  }
  .card-title {
    left: 124px; top: 59px; width: 14px;
    font-family: "Questrial", sans-serif; font-size: 12px; line-height: 14px; letter-spacing: 0.3px;
  }
  .card-contact {
    top: 0; height: 462px; text-align: end;
    font-weight: 700; font-size: 9px; line-height: 13px;
  }
  .card-contact.phones { left: 82px; width: 26px; }
  .card-contact.mobile { left: 47px; width: 26px; }
  .card-contact.online { left: 10px; width: 26px; }
  .card-brand {
    left: 207px; top: 0; height: 462px; width: 28px; text-align: end;
    font-weight: 700; font-size: 24px; line-height: 28px; letter-spacing: 1px; text-transform: uppercase;
  }
</style>
</head>
<body>
  <header class="letterhead-header">
    <div class="brand-name">Ridgemoor</div>
  </header>

  <footer class="letterhead-footer">
    <div class="footer-col phones">Cairns Phone: 07 40551926<br>Weipa Phone: 07 40613847</div>
    <div class="footer-col mobile">Mobile: 0491 570 384<br>Fax: 07 40338172</div>
    <div class="footer-col online">email: admin@ridgemoorholdings-example.com.au<br>ABN 51 824 306 917</div>
  </footer>

  <section class="business-card">
    <div class="vertical card-name">NAME</div>
    <div class="vertical card-title">PRESIDENT DIRECTOR</div>
    <div class="vertical card-brand">Ridgemoor</div>
    <div class="vertical card-contact phones">Cairns Phone: 07 40551926<br>Weipa Phone: 07 40613847</div>
    <div class="vertical card-contact mobile">Mobile: 0491 570 384<br>Fax: 07 40338172</div>
    <div class="vertical card-contact online">email: admin@ridgemoorholdings-example.com.au<br>ABN 51 824 306 917</div>
  </section>
</body>
</html>
```